Wrenfield Sailing Club Stationary
Wrenfield Sailing Club
Project: Wrenfield Sailing Club Stationary
Wrenfield Sailing Club Stationary - Outdoors
Creative Brief
Modern
Derek Omsted
Commodore
P.O. Box 58047 Columbus , OH 43118
wsc@wrenfieldsailing.example
wrenfieldsailing.example
Use Colors of logo. Blue and Red 1. blue : C= 85, M= 50, Y= 0, K= 50 2. red : C= 15, M= 100, Y= 90, K= 50

```html
<!DOCTYPE html>
<html lang="en">
<head>
<meta charset="utf-8">
<title>Wrenfield Sailing Club Stationery</title>
<link href="https://fonts.googleapis.com/css2?family=Montserrat:wght@400;600;700&display=swap" rel="stylesheet">
<style>
  :root{
    --navy:#1f4585;
    --red:#8e1f2b;
    --paper:#ffffff;
    --paper-shade:#eef0f4;
    --ink:#3a3f4a;
    --faint:#dfe3ea;
    --backdrop:#e6e2dc;
    --label:#7a7268;
  }
  *{box-sizing:border-box;margin:0;padding:0}
  html,body{width:1200px;height:466px;overflow:hidden}
  body{background:var(--backdrop);font-family:"Montserrat",Arial,sans-serif;color:var(--ink);position:relative}
  .piece{position:absolute;background:var(--paper);box-shadow:0 2px 6px rgba(0,0,0,.18);overflow:hidden}
  .piece svg.art{position:absolute;inset:0;width:100%;height:100%}
  .label{position:absolute;font-size:6px;letter-spacing:1px;text-transform:uppercase;color:var(--label);font-weight:600;white-space:nowrap}
  .mark{display:flex;align-items:center;gap:4px;font-weight:600;color:var(--navy);white-space:nowrap;position:absolute}
  .mark .dot{border-radius:50%;background:var(--navy);flex:none}
  .mark.light{color:var(--paper)}
  .mark.light .dot{background:var(--paper)}
  .contact{position:absolute;font-size:5px;line-height:1.5;color:var(--ink)}
  .contact strong{font-weight:600;color:var(--navy)}

  .card{width:96px;height:54px;left:30px}
  .card-front{top:170px}
  .card-back{top:244px;background:var(--navy)}
  .card .mark{font-size:4.6px;gap:3px}
  .card .mark .dot{width:5px;height:5px}
  .card-front .mark{left:7px;top:7px}
  .card-front .contact{left:7px;top:18px;font-size:3.4px;white-space:nowrap}
  .card-back .mark{left:0;right:0;top:0;bottom:0;justify-content:center}

  .letterhead{width:276px;height:390px;top:30px}
  .letterhead-one{left:220px}
  .letterhead-two{left:520px}
  .watermark{position:absolute;left:0;right:0;top:160px;text-align:center;font-weight:600;font-size:30px;line-height:1.1;color:var(--faint)}

  .envelope{width:330px;height:78px;left:840px}
  .envelope-blue{top:32px}
  .envelope-red{top:118px}
  .envelope-plain{top:204px}
  .envelope-wave{left:870px;top:300px;width:290px;height:120px}
</style>
</head>
<body>

<span class="label" style="left:30px;top:160px">Stationery Concepts</span>

<div class="piece card card-front">
  <div class="mark"><span class="dot"></span>Wrenfield Sailing Club</div>
  <div class="contact">
    <strong>Derek Omsted</strong> · Commodore<br>
    P.O. Box 58047 Columbus , OH 43118<br>
    wsc@wrenfieldsailing.example<br>
    wrenfieldsailing.example
  </div>
</div>
<span class="label" style="left:30px;top:229px">Business Card Front</span>

<div class="piece card card-back">
  <div class="mark light"><span class="dot"></span>Wrenfield Sailing Club</div>
</div>
<span class="label" style="left:30px;top:303px">Business Card Back</span>

<div class="piece letterhead letterhead-one">
  <svg class="art" viewBox="0 0 276 390" preserveAspectRatio="none" aria-hidden="true">
    <path d="M230 0 H276 V330 C262 220 258 120 230 0 Z" fill="var(--navy)"/>
    <path d="M244 0 C262 110 268 220 276 300 V0 Z" fill="var(--red)"/>
    <path d="M0 300 C70 360 170 380 276 372 V390 H0 Z" fill="var(--red)"/>
    <path d="M0 330 C80 378 180 390 276 382 V390 H0 Z" fill="var(--navy)"/>
  </svg>
  <div class="mark" style="left:86px;top:22px;font-size:7px"><span class="dot" style="width:9px;height:9px"></span>Wrenfield Sailing Club</div>
  <div class="contact" style="left:22px;top:268px">
    <strong>Derek Omsted</strong>, Commodore<br>
    P.O. Box 58047 Columbus , OH 43118<br>
    wsc@wrenfieldsailing.example<br>
    wrenfieldsailing.example
  </div>
</div>
<span class="label" style="left:300px;top:426px">Letterhead Option 1</span>

<div class="piece letterhead letterhead-two">
  <svg class="art" viewBox="0 0 276 390" preserveAspectRatio="none" aria-hidden="true">
    <path d="M0 345 C90 320 190 330 276 355 V390 H0 Z" fill="var(--red)"/>
    <path d="M0 360 C90 338 190 348 276 372 V390 H0 Z" fill="var(--navy)"/>
  </svg>
  <div class="mark" style="left:86px;top:22px;font-size:7px"><span class="dot" style="width:9px;height:9px"></span>Wrenfield Sailing Club</div>
  <div class="watermark">Wrenfield<br>Sailing Club</div>
  <div class="contact" style="left:0;right:0;top:377px;text-align:center;color:var(--paper);font-size:4.5px">
    P.O. Box 58047 Columbus , OH 43118 · wsc@wrenfieldsailing.example · wrenfieldsailing.example
  </div>
</div>
<span class="label" style="left:600px;top:426px">Letterhead Option 2</span>

<div class="piece envelope envelope-blue" style="background:var(--navy)">
  <svg class="art" viewBox="0 0 330 78" preserveAspectRatio="none" aria-hidden="true">
    <path d="M0 0 L165 46 L330 0" fill="none" stroke="var(--paper-shade)" stroke-opacity=".35" stroke-width="1"/>
  </svg>
</div>
<div class="piece envelope envelope-red" style="background:var(--red)">
  <svg class="art" viewBox="0 0 330 78" preserveAspectRatio="none" aria-hidden="true">
    <path d="M0 0 L165 46 L330 0" fill="none" stroke="var(--paper-shade)" stroke-opacity=".35" stroke-width="1"/>
    <circle cx="165" cy="46" r="4" fill="var(--paper)"/>
  </svg>
</div>
<div class="piece envelope envelope-plain">
  <svg class="art" viewBox="0 0 330 78" preserveAspectRatio="none" aria-hidden="true">
    <path d="M0 0 L165 40 L330 0" fill="none" stroke="var(--faint)" stroke-width="1"/>
  </svg>
  <div class="mark" style="left:128px;top:48px;font-size:5px"><span class="dot" style="width:6px;height:6px"></span>Wrenfield Sailing Club</div>
</div>
<span class="label" style="left:1000px;top:288px">Envelope Options</span>

<div class="piece envelope-wave">
  <svg class="art" viewBox="0 0 290 120" preserveAspectRatio="none" aria-hidden="true">
    <path d="M200 0 H290 V60 C270 30 240 10 200 0 Z" fill="var(--navy)"/>
    <path d="M0 70 C50 100 150 112 290 106 V120 H0 Z" fill="var(--navy)"/>
    <path d="M0 90 C60 112 160 118 290 114 V120 H0 Z" fill="var(--red)"/>
  </svg>
  <div class="mark" style="left:14px;top:12px;font-size:5px"><span class="dot" style="width:6px;height:6px"></span>Wrenfield Sailing Club</div>
  <div class="contact" style="left:14px;top:22px;font-size:4px">P.O. Box 58047 Columbus , OH 43118</div>
</div>

</body>
</html>
```